Design refresh of existing HR Application

QuillStaff is an HR & Payroll processing software, already in use by thousands of people. It is a feature packed, enterprise-grade software that is also simple and user friendly. Visit us at https://quillstaff.example

Seeking a refresh of the app design/UI.

Key objectives are to make it "sleeker", more professional and polished, whist still retaining functionality. Not intended to be a massive overhaul, but more of reorganization and improvements on design elements.

You may login to our demo account to see the app live.
https://app.quillstaff.example/login
User: demo@quillstaff.example
Password: Zip20

Target Market(s)

HR Managers, business administrators/owners and employees.

Industry/Entity Type

Business Software

Number of Pages Required

4 page

Font styles to use
Other font styles liked:
• Lato

Colors
0255a3
3377b5
00a990
33b8a4
f37122
faa54b

Requirements
Must have
• Must retain the current functionality on each page.
Nice to have
• Fine to suggest changes to colors, font sizes, card designs, moving sections around and any other design element changes.

```html
<!DOCTYPE html>
<html lang="en">
<head>
<meta charset="utf-8">
<title>QuillStaff – Dashboard</title>
<link href="https://fonts.googleapis.com/css2?family=Poppins:wght@400;500;600;700&display=swap" rel="stylesheet">
<style>
:root{
  --teal:#00a8c6;
  --teal-text:#0a86a3;
  --bg:#e3e9ed;
  --card:#ffffff;
  --panel:#f3f6f8;
  --line:#d4dde3;
  --ink:#1e2b37;
  --muted:#55616c;
  --orange:#f37122;
  --amber:#f6b42f;
  --gold:#f2a81d;
  --green:#5fd68a;
  --red:#c4151c;
  --cream:#fdf1d8;
}
*{box-sizing:border-box;margin:0;padding:0}
html,body{width:1200px;height:900px;overflow:hidden}
body{font-family:'Poppins',sans-serif;background:var(--bg);color:var(--ink);position:relative}
.sidebar{position:absolute;left:0;top:0;width:74px;height:900px;background:#fff}
.brand{position:absolute;top:22px;left:0;width:74px;text-align:center;font-size:9px;font-weight:600;color:var(--teal-text)}
.brand .mark{display:block;width:22px;height:22px;margin:0 auto 4px;background:var(--teal-text);border-radius:4px}
.nav{position:absolute;top:88px;left:0;width:74px}
.nav-item{display:flex;flex-direction:column;align-items:center;color:var(--teal-text);font-size:6.3px;text-transform:uppercase;position:absolute;left:0;width:74px}
.nav-item svg{width:20px;height:20px;margin-bottom:3px}
.powered{position:absolute;bottom:22px;left:0;width:74px;text-align:center;font-size:5.5px;color:var(--muted)}
.powered b{display:block;font-size:9px;font-weight:500;color:var(--teal-text);margin-top:10px}
.topbar{position:absolute;left:74px;top:0;width:1126px;height:50px;background:var(--teal)}
.btn-create{position:absolute;left:14px;top:12px;width:128px;height:28px;background:#fff;border-radius:2px;font-size:8px;display:flex;align-items:center;justify-content:center;color:var(--ink)}
.lang{position:absolute;left:898px;top:14px;width:44px;height:22px;background:#fff;border-radius:2px;display:flex;font-size:8px;color:var(--teal-text);font-weight:500}
.lang span{flex:1;display:flex;align-items:center;justify-content:center}
.lang span+span{border-left:1px solid var(--line);color:var(--orange)}
.help{position:absolute;left:954px;top:14px;width:22px;height:22px;background:#fff;border-radius:2px;color:var(--teal);font-weight:600;font-size:13px;display:flex;align-items:center;justify-content:center}
.user{position:absolute;left:1000px;top:13px;display:flex;align-items:center;color:#fff;font-size:7.5px;line-height:10px}
.avatar-lg{width:24px;height:24px;border-radius:50%;background:#3a3a3a;border:2px solid #fff;margin-right:6px}
.card{position:absolute;background:var(--card);border-radius:10px;overflow:hidden}
.title{font-size:9.5px;color:var(--teal-text);text-transform:uppercase;position:absolute;padding-bottom:3px;border-bottom:2px solid var(--amber)}
.title.dark{color:var(--ink);border:0;font-size:8.5px;font-weight:500}
.illus{position:absolute;border-radius:4px}
.greet-top{position:absolute;left:0;top:0;width:100%;height:92px;background:var(--amber)}
.greet-top p{position:absolute;left:119px;top:30px;color:#fff;font-size:11px}
.greet-top h2{position:absolute;left:119px;top:44px;color:#fff;font-size:18px;font-weight:700}
.no-events{position:absolute;left:160px;top:150px;font-size:11.5px;line-height:17px;color:#2d3b48}
.sched-head{position:absolute;left:0;top:0;width:100%;height:44px;background:var(--panel)}
.month{position:absolute;left:28px;top:52px;font-size:10px;color:#2d3b48}
.arrows{position:absolute;right:28px;top:50px;font-size:12px;color:var(--muted);letter-spacing:8px}
.cal{position:absolute;left:20px;top:78px;width:200px;display:grid;grid-template-columns:repeat(7,1fr);row-gap:12px;text-align:center;font-size:8.5px;color:#2d3b48}
.cal span{position:relative;height:16px;line-height:16px}
.cal .o::after,.cal .g::after{content:"";position:absolute;left:50%;bottom:-3px;width:2px;height:2px;margin-left:-1px;border-radius:50%;background:var(--orange)}
.cal .g::after{background:#2bb673}
.cal .dim{color:#9aa4ad}
.cal .today{background:var(--orange);color:#fff;border-radius:4px;width:22px;height:22px;line-height:22px;margin:-3px auto 0}
.off-head{position:absolute;left:0;top:0;width:100%;height:44px;background:var(--panel)}
.btn-req{position:absolute;right:13px;top:7px;width:100px;height:29px;background:var(--orange);color:#fff;font-size:9.5px;font-weight:500;border-radius:3px;display:flex;align-items:center;justify-content:center}
.stat{position:absolute;top:79px;width:215px;height:112px;background:var(--panel);border:1px solid var(--line);border-radius:10px}
.stat .lbl{position:absolute;left:26px;top:72px;font-size:8px;color:#2d3b48}
.stat .num{position:absolute;right:40px;top:26px;font-size:30px;font-weight:600;color:var(--teal-text);width:40px;text-align:center}
.stat .sub{position:absolute;right:30px;top:70px;font-size:8px;color:#2d3b48;width:60px;text-align:center}
.ql{position:absolute;top:16px;width:222px;height:78px;background:var(--panel);border:1px solid var(--line);border-radius:10px}
.ql svg{position:absolute;left:24px;top:26px;width:24px;height:24px}
.ql .lbl{position:absolute;left:56px;top:27px;font-size:8px;line-height:9px;color:#2d3b48}
.ql .num{position:absolute;right:20px;top:18px;width:41px;height:41px;background:#fff;border:1px solid var(--line);border-radius:6px;font-size:18px;font-weight:600;color:var(--teal-text);display:flex;align-items:center;justify-content:center}
.rows{position:absolute;left:20px;top:60px;width:270px}
.row{display:flex;align-items:center;height:20px;font-size:7.5px;color:#2d3b48}
.face{width:16px;height:16px;border-radius:50%;background:#6b4a3a;margin-right:10px;flex:none}
.face.b{background:#1d6fa3}.face.c{background:#4f8a5a}
.row .n{width:120px}.row .p{flex:1}.row .v{width:12px}
.scroll{position:absolute;width:3px;background:#edf1f3;border-radius:2px}
.scroll i{display:block;width:3px;background:var(--teal);border-radius:2px}
.filter{position:absolute;right:52px;top:22px;font-size:7px;color:var(--muted)}
.dots{position:absolute;right:20px;top:19px;font-size:10px;color:var(--muted);letter-spacing:-1px}
.leave{position:absolute;width:138px;height:58px;border:1px solid var(--line);border-radius:5px;background:#fff}
.leave .who{position:absolute;left:34px;top:8px;font-size:7px;line-height:11px;color:#2d3b48}
.leave .face{position:absolute;left:11px;top:12px;width:15px;height:15px}
.tag{position:absolute;left:11px;bottom:8px;width:115px;height:12px;border-radius:2px;color:#fff;font-size:6.5px;font-weight:500;display:flex;align-items:center;justify-content:center}
.menu{position:absolute;left:219px;top:38px;width:93px;background:#fff;border:1px solid var(--line);box-shadow:0 2px 6px rgba(0,0,0,.12);font-size:6px;color:#2d3b48}
.menu div{height:20.5px;line-height:20.5px;padding-left:11px;border-top:1px solid var(--line)}
.menu div:first-child{border:0}
.starred{position:absolute;right:26px;font-size:7.5px;color:#2d3b48}
.notes{position:absolute;left:25px;top:52px;width:348px}
.note{position:relative;height:20px;margin-bottom:3.6px;background:var(--panel);font-size:7.2px;line-height:20px;padding-left:11px;color:#2d3b48;white-space:nowrap}
.note::after{content:"‹";position:absolute;right:8px;top:0;color:var(--muted);font-size:10px}
.note.hi{background:var(--cream);padding-right:40px}
.note.hi::after{content:none}
.act{position:absolute;top:0;width:18px;height:20px;display:flex;align-items:center;justify-content:center;color:#fff;font-size:8px}
.empty{position:absolute;left:0;width:100%;text-align:center;font-size:7.5px;color:#2d3b48}
.ann{position:absolute;left:29px;top:39px;width:485px;height:36px;background:var(--cream);font-size:7.3px;line-height:11px;color:#2d3b48;padding:6px 50px 0 10px}
</style>
</head>
<body>

<aside class="sidebar">
  <div class="brand"><span class="mark"></span>QuillStaff</div>
  <nav class="nav">
    <div class="nav-item" style="top:0"><svg viewBox="0 0 24 24" fill="none" stroke="#0a86a3" stroke-width="1.5"><rect x="3" y="3" width="18" height="18" rx="3"/><rect x="8" y="7" width="6" height="6" stroke="#f37122"/><rect x="10" y="10" width="6" height="6"/></svg>Dashboard</div>
    <div class="nav-item" style="top:50px"><svg viewBox="0 0 24 24" fill="none" stroke="#0a86a3" stroke-width="1.5"><circle cx="8" cy="8" r="3" stroke="#f37122"/><circle cx="16" cy="7" r="3"/><path d="M2 20c0-4 3-6 6-6s6 2 6 6M12 14c1-1 2-2 4-2 3 0 6 2 6 6"/></svg>Employees</div>
    <div class="nav-item" style="top:106px"><svg viewBox="0 0 24 24" fill="none" stroke="#0a86a3" stroke-width="1.5"><rect x="3" y="5" width="18" height="16" rx="2"/><path d="M3 10h18M8 3v4M16 3v4"/><rect x="6" y="13" width="5" height="4" fill="#0a86a3"/><circle cx="15" cy="14" r="1" fill="#f37122"/><circle cx="18" cy="14" r="1" fill="#f37122"/></svg>Calendar</div>
    <div class="nav-item" style="top:162px"><svg viewBox="0 0 24 24" fill="none" stroke="#0a86a3" stroke-width="1.5"><rect x="4" y="3" width="16" height="18" rx="2"/><path d="M13 9h4M13 13h4" stroke="#f37122"/><text x="6" y="15" font-size="9" fill="#0a86a3" stroke="none">$</text></svg>Expenses</div>
    <div class="nav-item" style="top:224px"><svg viewBox="0 0 24 24" fill="none" stroke="#0a86a3" stroke-width="1.5"><rect x="3" y="6" width="18" height="12" rx="2"/><path d="M12 10h6M12 14h6" stroke="#f37122"/><text x="5" y="16" font-size="9" fill="#0a86a3" stroke="none">$</text></svg>Payroll</div>
    <div class="nav-item" style="top:276px"><svg viewBox="0 0 24 24" fill="none" stroke="#0a86a3" stroke-width="1.5"><path d="M12 3c-4 4-6 7-6 10a6 6 0 0012 0c0-3-2-6-6-10z"/><path d="M3 21h18" stroke="#f37122"/></svg>Loans</div>
    <div class="nav-item" style="top:330px"><svg viewBox="0 0 24 24" fill="none" stroke="#f37122" stroke-width="1.5"><path d="M3 18l6-6 4 4 8-9"/><circle cx="9" cy="12" r="1.5" fill="#0a86a3" stroke="none"/><circle cx="13" cy="16" r="1.5" fill="#0a86a3" stroke="none"/></svg>Performance</div>
    <div class="nav-item" style="top:384px"><svg viewBox="0 0 24 24" fill="none" stroke="#0a86a3" stroke-width="1.5"><rect x="2" y="4" width="9" height="6" rx="1"/><rect x="13" y="4" width="9" height="6" rx="1" stroke="#f37122"/><path d="M4 16l4-3 4 3 4-3 4 3"/></svg>Engagement</div>
    <div class="nav-item" style="top:446px"><svg viewBox="0 0 24 24" fill="none" stroke="#0a86a3" stroke-width="1.5"><rect x="5" y="3" width="14" height="18" rx="2"/><path d="M8 9h8M8 13h8M8 17h5" stroke="#f37122"/></svg>Reports</div>
    <div class="nav-item" style="top:512px"><svg viewBox="0 0 24 24" fill="none" stroke="#0a86a3" stroke-width="1.5"><circle cx="12" cy="12" r="3" stroke="#f37122"/><path d="M12 2v3M12 19v3M2 12h3M19 12h3M5 5l2 2M17 17l2 2M5 19l2-2M17 7l2-2"/><circle cx="12" cy="12" r="7"/></svg>Settings</div>
  </nav>
  <div class="powered">Powered by<b>QuillStaff</b></div>
</aside>

<header class="topbar">
  <div class="btn-create">CREATE A COMPANY</div>
  <div class="lang"><span>EN</span><span>⌄</span></div>
  <div class="help">?</div>
  <div class="user"><div class="avatar-lg" role="img" aria-label="User profile photo"></div><div>Admin, Demo<br>HR Administrator</div><span style="margin-left:10px">⌄</span></div>
</header>

<section class="card" style="left:87.5px;top:64px;width:334px;height:223px">
  <div class="greet-top">
    <div class="illus" style="left:32px;top:26px;width:58px;height:40px;background:linear-gradient(180deg,#f9c95a,#f08a3a)" role="img" aria-label="Sunrise illustration"></div>
    <p>Good Morning Demo,</p>
    <h2>it's great to see you!</h2>
  </div>
  <div class="title dark" style="left:30px;top:119px">TODAY'S EVENT</div>
  <div class="illus" style="left:38px;top:142px;width:50px;height:48px;background:#d6efe9" role="img" aria-label="Celebration calendar illustration"></div>
  <div class="no-events">No scheduled<br>events today</div>
</section>

<section class="card" style="left:432.5px;top:64px;width:237.5px;height:223px">
  <div class="sched-head"><div class="title dark" style="left:28px;top:18px">MY SCHEDULE</div></div>
  <div class="month">MAY &nbsp;2020</div>
  <div class="arrows">‹ ›</div>
  <div class="cal">
    <span>1</span><span>2</span><span>3</span><span>4</span><span>5</span><span>6</span><span>7</span>
    <span class="o">8</span><span class="o">9</span><span class="o">10</span><span class="o">11</span><span class="o">12</span><span>13</span><span>14</span>
    <span class="o">15</span><span class="o">16</span><span class="o">17</span><span class="g">18</span><span class="o">19</span><span>20</span><span>21</span>
    <span class="o">22</span><span><b class="today" style="display:block;font-weight:500">23</b></span><span class="g">24</span><span class="o">25</span><span class="o">26</span><span class="o">27</span><span>28</span>
    <span class="o">29</span><span>30</span><span>31</span><span class="dim">1</span><span class="dim">2</span><span class="dim">3</span><span class="dim">4</span>
  </div>
</section>

<section class="card" style="left:680px;top:64px;width:507.5px;height:223px">
  <div class="off-head"><div class="title dark" style="left:28px;top:18px">MY TIME OFF</div><div class="btn-req">REQUEST</div></div>
  <div class="stat" style="left:27.5px">
    <div class="illus" style="left:38px;top:28px;width:34px;height:34px;background:#cfeef4" role="img" aria-label="Beach chair illustration"></div>
    <div class="lbl">ANNUAL LEAVE</div><div class="num">6</div><div class="sub">LEFT</div>
  </div>
  <div class="stat" style="left:266px">
    <div class="illus" style="left:36px;top:36px;width:46px;height:28px;background:#f9d892" role="img" aria-label="Sick bed illustration"></div>
    <div class="lbl" style="left:36px;top:74px">SICK DAYS</div><div class="num">1</div><div class="sub">TAKEN</div>
  </div>
</section>

<section class="card" style="left:87.5px;top:297px;width:1100px;height:112px">
  <div class="title" style="left:21px;top:49px;border-bottom-color:var(--amber)">QUICK LINKS</div>
  <div class="ql" style="left:106.5px">
    <svg viewBox="0 0 24 24" fill="none" stroke="#f2a81d" stroke-width="1.5"><rect x="2" y="4" width="20" height="18" rx="2"/><path d="M2 9h20M7 2v4M17 2v4M12 12v6M9 15h6" /></svg>
    <div class="lbl">EVENT<br>AMENDMENTS</div><div class="num">12</div>
  </div>
  <div class="ql" style="left:355px">
    <svg viewBox="0 0 24 24" fill="none" stroke="#f2a81d" stroke-width="1.5"><rect x="6" y="4" width="16" height="12"/><path d="M6 4l8 6 8-6"/><path d="M2 20l6-8" stroke="#0a86a3"/></svg>
    <div class="lbl">LEAVE<br>REQUESTS</div><div class="num">2</div>
  </div>
  <div class="ql" style="left:603.5px">
    <svg viewBox="0 0 24 24" fill="none" stroke="#f2a81d" stroke-width="1.5"><circle cx="11" cy="12" r="9"/><path d="M11 12H6" stroke="#0a86a3"/><circle cx="19" cy="18" r="4" fill="#fff" stroke="#0a86a3"/><path d="M19 16v4M17 18h4" stroke="#0a86a3"/></svg>
    <div class="lbl">EVENT<br>REQUESTS</div><div class="num">07</div>
  </div>
  <div class="ql" style="left:854.5px">
    <svg viewBox="0 0 24 24" fill="none" stroke="#f2a81d" stroke-width="1.5"><circle cx="12" cy="12" r="10"/><text x="7.5" y="17" font-size="13" fill="#0a86a3" stroke="none">$</text></svg>
    <div class="lbl">PAYROLLS<br>PENDING</div><div class="num">01</div>
  </div>
</section>

<section class="card" style="left:87.5px;top:419px;width:335px;height:279px">
  <div class="title" style="left:21px;top:23px">TARDY TODAY</div>
  <div class="rows">
    <div class="row"><span class="face" role="img" aria-label="Employee photo"></span><span class="n">67, Employee</span><span class="p">Logistic Officer</span><span class="v">5.5</span></div>
    <div class="row"><span class="face b" role="img" aria-label="Employee photo"></span><span class="n">67, Employee</span><span class="p">QA Manager</span><span class="v">5.5</span></div>
    <div class="row"><span class="face" role="img" aria-label="Employee photo"></span><span class="n">95, Employee</span><span class="p">Factory Worker</span><span class="v">5.5</span></div>
    <div class="row"><span class="face c" role="img" aria-label="Employee photo"></span><span class="n">95, Employee</span><span class="p">Factory Worker</span><span class="v">5.5</span></div>
    <div class="row"><span class="face" role="img" aria-label="Employee photo"></span><span class="n">75, Employee</span><span class="p">Postion 15</span><span class="v">5.5</span></div>
    <div class="row"><span class="face b" role="img" aria-label="Employee photo"></span><span class="n">75, Employee</span><span class="p">Postion 3</span><span class="v">5.5</span></div>
    <div class="row"><span class="face" role="img" aria-label="Employee photo"></span><span class="n">14, Employee</span><span class="p">Postion 13</span><span class="v">5.5</span></div>
    <div class="row"><span class="face c" role="img" aria-label="Employee photo"></span><span class="n">14, Employee</span><span class="p">Postion 13</span><span class="v">5.5</span></div>
    <div class="row"><span class="face" role="img" aria-label="Employee photo"></span><span class="n">Employee, 447</span><span class="p">Postion 4</span><span class="v">5.5</span></div>
    <div class="row"><span class="face b" role="img" aria-label="Employee photo"></span><span class="n">Employee, 447</span><span class="p">Postion 1</span><span class="v">5.5</span></div>
  </div>
  <div class="scroll" style="left:318px;top:45px;height:214px"><i style="height:63px"></i></div>
</section>

<section class="card" style="left:432.5px;top:419px;width:335px;height:279px">
  <div class="title" style="left:25px;top:23px">WHO'S ON LEAVE TODAY</div>
  <div class="filter">⏷ Filter</div>
  <div class="dots">⋮</div>
  <div class="leave" style="left:25px;top:62px">
    <span class="face" role="img" aria-label="Employee photo"></span>
    <div class="who">34, Employee<br>HR Administrator</div>
    <div class="tag" style="background:var(--green)">Maternity Leave</div>
  </div>
  <div class="leave" style="left:173px;top:62px">
    <span class="face" role="img" aria-label="Employee photo"></span>
    <div class="who">14, Employee<br>Manager</div>
    <div class="tag" style="background:var(--amber)">Sick Leave</div>
  </div>
  <div class="leave" style="left:25px;top:132px">
    <span class="face" role="img" aria-label="Employee photo"></span>
    <div class="who">30, Employee<br>Jr HR admin</div>
    <div class="tag" style="background:var(--red)">Emergency Leave</div>
  </div>
  <div class="menu"><div>Same Department</div><div>Same Branch</div><div>Subordinates</div></div>
</section>

<section class="card" style="left:777.5px;top:422px;width:410px;height:278px">
  <div class="title" style="left:25px;top:20px">NOTIFICATIONS</div>
  <div class="starred" style="top:22px">☆ View Starred</div>
  <div class="notes">
    <div class="note hi">Rahman, Dewi has remotely checked in for Working on 20/05/2020 02:07<span style="position:absolute;right:44px;color:var(--muted)">›</span><span class="act" style="right:18px;background:var(--orange)">☆</span><span class="act" style="right:0;background:var(--red)">▪</span></div>
    <div class="note">Rahman, Dewi requests amendment on 15 Apr 2020 from 09:00 - 18:00.</div>
    <div class="note">Overtime request for Rahman, Dewi - 18 May 2020 at 19:00 | 21:00 Branch A</div>
    <div class="note">Rahman, Dewi requests Sick Leave on 19 May 2020.</div>
    <div class="note">Rahman, Dewi requests amendment on 30 Apr 2020 from 10:00 - 18:00.</div>
    <div class="note">Rahman, Dewi requests amendment on 11 May 2020 from 10:00 - 18:00.</div>
    <div class="note">Lowe, Martin (Marty) has declined Overtime on 12 Dec 2019.</div>
    <div class="note">Sick Leave on 02 Jan 2020 has been approved.</div>
    <div class="note">Lowe, Martin (Marty) has declined Overtime on 12 Dec 2019.</div>
  </div>
  <div class="scroll" style="left:384px;top:43px;height:214px"><i style="height:63px"></i></div>
</section>

<section class="card" style="left:87.5px;top:709px;width:544px;height:177px">
  <div class="title" style="left:24px;top:18px">EMPLOYEE UPDATES</div>
  <div class="starred" style="top:21px;right:18px">☆ View Starred</div>
  <div class="empty" style="top:91px;left:-5px">There are no Announcements</div>
</section>

<section class="card" style="left:641px;top:709px;width:546.5px;height:177px">
  <div class="title" style="left:29px;top:18px">ANNOUNCEMENTS</div>
  <div class="starred" style="top:21px;right:27px">☆ View Starred</div>
  <div class="ann">Free Friday drinks are available in the pantry on every week until the end of this year. Take the opportunity to get to know more people!
    <span style="position:absolute;right:44px;top:10px;color:var(--muted)">‹</span>
    <span class="act" style="right:18px;height:36px;background:var(--orange)">☆</span>
    <span class="act" style="right:0;height:36px;background:var(--red)">▪</span>
  </div>
  <div class="scroll" style="left:520px;top:39px;height:118px"><i style="height:63px"></i></div>
</section>

</body>
</html>
```